Business Card Design Project

Business and Appointment Card for Medical Practice. On back of card we would like to have: blank line for patient name, Mon-Fri each with a check box next to the day, blank line for appointment date, blank line for appointment time, with option to circle am or pm.

Target Market(s)

Professional Business Associates, as well as function as patient appointment cards (on back side of card)

Industry/Entity Type

Business

Colors

Designer to choose colors to be used in the design.

```html
<!DOCTYPE html>
<html lang="en">
<head>
<meta charset="utf-8">
<title>Rowan Hill Medical Associates – Business &amp; Appointment Card</title>
<link rel="stylesheet" href="https://fonts.googleapis.com/css2?family=Lato:wght@400;700&display=swap">
<style>
  :root {
    --backdrop: #2b2b2b;
    --card-white: #fbfbfb;
    --brand-red: #8e1a1c;
    --brand-red-dark: #741416;
    --label-red: #b8282c;
    --brand-green: #1f6e32;
    --rule: #2a2a2a;
    --box: #333333;
    --on-red: #f3e6e6;
  }
  * { box-sizing: border-box; margin: 0; padding: 0; }
  html, body { width: 1200px; height: 900px; overflow: hidden; }
  body {
    background: var(--backdrop);
    font-family: "Lato", Arial, sans-serif;
    position: relative;
  }
  .card {
    position: absolute;
    width: 640px;
    height: 366px;
    background: var(--card-white);
    border-radius: 4px;
    overflow: hidden;
    box-shadow: 0 12px 28px rgba(0,0,0,0.45);
  }

  /* ---------- Appointment side ---------- */
  .appointment-card { left: 60px; top: 60px; }
  .appointment-card .brand {
    position: absolute; left: 36px; top: 112px;
    display: flex; align-items: center; gap: 10px;
  }
  .brand-dot {
    width: 22px; height: 22px; border-radius: 50%;
    background: var(--brand-red);
  }
  .brand-name {
    font-weight: 700; color: var(--brand-green);
    line-height: 1.15; letter-spacing: 0.5px;
  }
  .appointment-card .brand-name { font-size: 19px; }
  .appointment-pill {
    position: absolute; right: 36px; top: 30px;
    background: var(--label-red); color: #fff;
    font-size: 17px; letter-spacing: 1.5px;
    padding: 6px 26px; border-radius: 16px;
    text-transform: uppercase; font-weight: 400;
  }
  .rule { position: absolute; height: 2px; background: var(--rule); }
  .rule-name { left: 270px; right: 36px; top: 106px; }
  .label { position: absolute; font-weight: 700; font-size: 16px; }
  .label.green { color: var(--brand-green); }
  .label.red { color: var(--label-red); }
  .label-patient { left: 330px; top: 114px; }
  .days {
    position: absolute; left: 36px; right: 36px; top: 172px;
    display: flex; justify-content: space-between;
  }
  .day { display: flex; align-items: center; gap: 8px; font-weight: 700; font-size: 16px; }
  .day.green { color: var(--brand-green); }
  .day.red { color: var(--label-red); }
  .checkbox {
    width: 22px; height: 22px; border: 2.5px solid var(--box);
    border-radius: 5px; background: #fff;
  }
  .rule-date { left: 36px; right: 36px; top: 244px; }
  .label-date { left: 36px; top: 258px; }
  .label-time { left: 300px; top: 258px; }
  .rule-time { left: 300px; right: 36px; top: 318px; }
  .label-am { left: 420px; top: 292px; }
  .label-pm { right: 40px; top: 292px; }

  /* ---------- Business side ---------- */
  .business-card { left: 500px; top: 470px; }
  .business-card .brand {
    position: absolute; left: 0; right: 0; top: 78px;
    display: flex; justify-content: center; align-items: center; gap: 14px;
  }
  .business-card .brand-dot { width: 30px; height: 30px; }
  .business-card .brand-name { font-size: 30px; text-align: left; }
  .contact-band {
    position: absolute; left: 0; right: 0; bottom: 0; height: 170px;
    background: linear-gradient(180deg, var(--brand-red) 0%, var(--brand-red-dark) 100%);
  }
  .person { position: absolute; left: 34px; bottom: 32px; color: var(--on-red); }
  .person-name { font-size: 22px; font-weight: 700; letter-spacing: 0.5px; color: #fff; }
  .person-role { font-size: 17px; margin-top: 2px; }
  .contact-list {
    position: absolute; left: 318px; top: 18px; list-style: none;
    color: var(--on-red); font-size: 14.5px;
  }
  .contact-list li { display: flex; align-items: center; gap: 12px; height: 26px; }
  .contact-list svg { width: 16px; height: 16px; flex: none; }
</style>
</head>
<body>

<section class="card appointment-card" aria-label="Appointment card">
  <div class="brand">
    <span class="brand-dot"></span>
    <span class="brand-name">Rowan Hill<br>Medical Associates</span>
  </div>
  <div class="appointment-pill">Appointment Card</div>

  <div class="rule rule-name"></div>
  <span class="label green label-patient">Patient Name</span>

  <div class="days">
    <span class="day red">Mon <span class="checkbox"></span></span>
    <span class="day green">Tue <span class="checkbox"></span></span>
    <span class="day red">Wed <span class="checkbox"></span></span>
    <span class="day green">Thu <span class="checkbox"></span></span>
    <span class="day red">Fri <span class="checkbox"></span></span>
  </div>

  <div class="rule rule-date"></div>
  <span class="label green label-date">Date:</span>
  <span class="label red label-time">Time:</span>
  <span class="label green label-am">AM</span>
  <span class="label red label-pm">PM</span>
  <div class="rule rule-time"></div>
</section>

<section class="card business-card" aria-label="Business card">
  <div class="brand">
    <span class="brand-dot"></span>
    <span class="brand-name">Rowan Hill<br>Medical Associates</span>
  </div>

  <div class="contact-band">
    <ul class="contact-list">
      <li>
        <svg viewBox="0 0 16 16" fill="none" stroke="currentColor" stroke-width="1.5"><rect x="4" y="1" width="8" height="14" rx="1.5"/><line x1="7" y1="12.5" x2="9" y2="12.5"/></svg>
        07700 900418
      </li>
      <li>
        <svg viewBox="0 0 16 16"><circle cx="8" cy="8" r="7" fill="currentColor"/></svg>
        daniel.hartley_rhm
      </li>
      <li>
        <svg viewBox="0 0 16 16" fill="none" stroke="currentColor" stroke-width="1.5"><rect x="1" y="3" width="14" height="10" rx="1"/><polyline points="1,3 8,9 15,3"/></svg>
        daniel.hartley@rowanhillmedical.com
      </li>
      <li>
        <svg viewBox="0 0 16 16" fill="none" stroke="currentColor" stroke-width="1.6" stroke-linecap="round"><path d="M7 9.5l-2 2a2.1 2.1 0 0 1-3-3l2-2a2.1 2.1 0 0 1 3 0"/><path d="M9 6.5l2-2a2.1 2.1 0 0 1 3 3l-2 2a2.1 2.1 0 0 1-3 0"/><line x1="6" y1="10" x2="10" y2="6"/></svg>
        www.rowanhillmedical.com
      </li>
    </ul>
    <div class="person">
      <div class="person-name">DANIEL HARTLEY</div>
      <div class="person-role">Founder</div>
    </div>
  </div>
</section>

</body>
</html>
```